High-end construction company needs a business card design

We need a modern looking business card that draws people in, is memorable and looks so good people will want to sick it on their fridges.
On the first side what is needed are:
Logo
My name - Tomas Verbelk
Title - Managing Director
Website - www.kravel.co.uk
Email - tomas@kravel.co.uk
Telephone - 020 5194 6381
Mobile - 07845319027
On the back side was is needed is a list of all the services we provide:
-Kitchen Renovations
-Bathroom Renovations
-House Renovations
-Garage Conversions
-Extensions
-Loft Conversions
-Conservatories
-Carpentry
-Tiling
-Electrical
-Plumbing & Heating
-Bricklaying
-Landscaping
-Decorating
-Plastering
We would like the colours to be the same shades as on the logo with grey or black for the words.
Target Market(s)
Anyone who needs building work done
Contact Information for Business Card
This business card is for a construction company which strives to deliver excellent service and quality.
The look and feel of the card should represent this.
Requirements
Must have
- On the first side what is needed are:
Logo
My name - Tomas Verbelk
Title - Managing Director
Website - www.kravel.co.uk
Email - tomas@kravel.co.uk
Telephone - 020 5194 6381
Mobile - 07845319027
Nice to have
- Cool looking features

```html
<!DOCTYPE html>
<html lang="en">
<head>
<meta charset="utf-8">
<title>Kravel – Business Card</title>
<link rel="stylesheet" href="https://fonts.googleapis.com/css2?family=Open+Sans:wght@400;600;700&display=swap">
<style>
  :root {
    --brand-green: #3cb800;
    --logo-green: #5fe600;
    --paper: #ffffff;
    --ink: #1a1a1a;
    --label-green: #3cb800;
  }
  * { margin: 0; padding: 0; box-sizing: border-box; }
  html, body { width: 914px; height: 1200px; overflow: hidden; }
  body {
    background: var(--brand-green);
    font-family: "Open Sans", Arial, sans-serif;
    position: relative;
  }
  .card {
    position: absolute;
    left: 88px;
    width: 731px;
    height: 490px;
    background: var(--paper);
    overflow: hidden;
  }
  .card--front { top: 88px; }
  .card--back { top: 600px; }
  .card svg.band { position: absolute; left: 0; top: 0; }

  .brand {
    position: absolute;
    left: 74px;
    top: 136px;
    display: flex;
    align-items: center;
    gap: 12px;
    color: var(--logo-green);
    font-weight: 700;
    font-size: 50px;
    line-height: 1;
    letter-spacing: 1px;
  }
  .brand__mark {
    width: 28px; height: 28px;
    background: var(--logo-green);
  }

  .contact {
    position: absolute;
    left: 453px;
    top: 89px;
    font-size: 15px;
    line-height: 22.7px;
    color: var(--ink);
  }
  .contact__row { display: flex; }
  .contact__label { width: 48px; color: var(--label-green); }

  .person {
    position: absolute;
    left: 99px;
    top: 282px;
    color: var(--paper);
  }
  .person__name { font-size: 27px; font-weight: 700; line-height: 1.2; }
  .person__title { font-size: 15px; line-height: 1.2; }

  .services {
    position: absolute;
    top: 119px;
    font-size: 16px;
    line-height: 22.8px;
    color: var(--paper);
    list-style: none;
  }
  .services--left { left: 73px; }
  .services--right { left: 340px; }

  .back-web {
    position: absolute;
    left: 506px;
    top: 418px;
    font-size: 19.5px;
    color: var(--ink);
  }
</style>
</head>
<body>
  <section class="card card--front">
    <svg class="band" width="731" height="490" viewBox="0 0 731 490">
      <polygon points="24,244 522,244 300,465 24,465" fill="var(--brand-green)"/>
    </svg>
    <div class="brand"><span class="brand__mark"></span>KRAVEL</div>
    <div class="contact">
      <div class="contact__row"><span class="contact__label">T:</span>020 5194 6381</div>
      <div class="contact__row"><span class="contact__label">M:</span>07845319027</div>
      <div class="contact__row"><span class="contact__label">E:</span>tomas@kravel.co.uk</div>
      <div class="contact__row"><span class="contact__label">W:</span>www.kravel.co.uk</div>
    </div>
    <div class="person">
      <div class="person__name">Tomas Verbelk</div>
      <div class="person__title">Managing Director</div>
    </div>
  </section>

  <section class="card card--back">
    <svg class="band" width="731" height="490" viewBox="0 0 731 490">
      <polygon points="24,23 706,23 403,466 24,466" fill="var(--brand-green)"/>
    </svg>
    <ul class="services services--left">
      <li>Kitchen Renovations</li>
      <li>Bathroom Renovations</li>
      <li>House Renovations</li>
      <li>Garage Conversions</li>
      <li>Extensions</li>
      <li>Loft Conversions</li>
      <li>Conservatories</li>
      <li>Carpentry</li>
    </ul>
    <ul class="services services--right">
      <li>Tiling</li>
      <li>Electrical</li>
      <li>Plumbing &amp; Heating</li>
      <li>Bricklaying</li>
      <li>Landscaping</li>
      <li>Decorating</li>
      <li>Plastering</li>
    </ul>
    <div class="back-web">www.kravel.co.uk</div>
  </section>
</body>
</html>
```